Bright Orchard
Bright & Fun-filled
Talia Brennick
Certified Holistic Wellness Coach, NLP Practitioner
no address pls
talia@brightorchard.com
www.brightorchard.com
To love oneself is the beginning of a lifelong romance. --Edwin Tarrow

```html
<!DOCTYPE html>
<html lang="en">
<head>
<meta charset="utf-8">
<title>Bright Orchard — Business Card</title>
<link rel="stylesheet" href="https://fonts.googleapis.com/css2?family=Lato:wght@400;700&display=swap">
<style>
  :root {
    --backdrop: #e9e6e2;
    --card-white: #ffffff;
    --brand-pink: #e3195a;
    --rule-grey: #5b5b5b;
    --ink-grey: #555555;
    --text-light: #ffffff;
  }
  * { margin: 0; padding: 0; box-sizing: border-box; }
  html, body {
    width: 1200px;
    height: 780px;
    overflow: hidden;
    background: var(--backdrop);
    font-family: "Lato", sans-serif;
  }
  .canvas {
    position: relative;
    width: 1200px;
    height: 780px;
    display: flex;
    align-items: center;
    justify-content: center;
  }
  .business-card {
    position: relative;
    width: 1000px;
    height: 572px;
    border-radius: 32px;
    overflow: hidden;
    background: var(--card-white);
    box-shadow: 0 10px 30px rgba(0,0,0,0.18);
  }
  .brand-area {
    position: absolute;
    left: 0; top: 0;
    width: 100%;
    height: 352px;
    display: flex;
    align-items: center;
    justify-content: center;
    gap: 22px;
  }
  .brand-name {
    font-size: 96px;
    font-weight: 400;
    color: var(--ink-grey);
    letter-spacing: -1px;
    white-space: nowrap;
  }
  .brand-dot {
    width: 44px;
    height: 44px;
    border-radius: 50%;
    background: var(--brand-pink);
    margin-top: 8px;
  }
  .divider-rule {
    position: absolute;
    left: 0; top: 352px;
    width: 100%;
    height: 6px;
    background: var(--rule-grey);
  }
  .contact-band {
    position: absolute;
    left: 0; top: 358px;
    width: 100%;
    height: 214px;
    background: var(--brand-pink);
    color: var(--text-light);
  }
  .identity {
    position: absolute;
    right: 530px;
    top: 42px;
    text-align: right;
    white-space: nowrap;
  }
  .person-name {
    font-size: 30px;
    font-weight: 700;
    margin-bottom: 6px;
  }
  .person-role {
    font-size: 23px;
    font-weight: 400;
    line-height: 1.35;
  }
  .column-split {
    position: absolute;
    left: 500px;
    top: 40px;
    width: 2px;
    height: 120px;
    background: var(--text-light);
  }
  .contact-list {
    position: absolute;
    left: 524px;
    top: 38px;
    list-style: none;
  }
  .contact-item {
    display: flex;
    align-items: center;
    gap: 12px;
    font-size: 22px;
    height: 38px;
    white-space: nowrap;
  }
  .contact-icon { width: 20px; height: 20px; flex: none; }
</style>
</head>
<body>
<main class="canvas">
  <section class="business-card">
    <header class="brand-area">
      <span class="brand-name">Bright Orchard</span>
      <span class="brand-dot" aria-hidden="true"></span>
    </header>
    <div class="divider-rule"></div>
    <footer class="contact-band">
      <div class="identity">
        <p class="person-name">Talia Brennick</p>
        <p class="person-role">Certified Holistic Wellness Coach,<br>NLP Practitioner</p>
      </div>
      <div class="column-split"></div>
      <ul class="contact-list">
        <li class="contact-item">
          <svg class="contact-icon" viewBox="0 0 20 20" aria-hidden="true">
            <rect x="5" y="1" width="10" height="18" rx="2" fill="#fff"/>
            <rect x="7" y="4" width="6" height="9" fill="#e3195a"/>
          </svg>
          <span>555.014.2273</span>
        </li>
        <li class="contact-item">
          <svg class="contact-icon" viewBox="0 0 20 20" aria-hidden="true">
            <rect x="1" y="4" width="18" height="12" rx="1.5" fill="#fff"/>
            <path d="M2 5 L10 11 L18 5" fill="none" stroke="#e3195a" stroke-width="1.6"/>
          </svg>
          <span>talia@brightorchard.com</span>
        </li>
        <li class="contact-item">
          <svg class="contact-icon" viewBox="0 0 20 20" aria-hidden="true">
            <circle cx="10" cy="10" r="8.5" fill="#fff"/>
            <path d="M1.5 10 H18.5 M10 1.5 C6 6 6 14 10 18.5 M10 1.5 C14 6 14 14 10 18.5" fill="none" stroke="#e3195a" stroke-width="1.3"/>
          </svg>
          <span>www.brightorchard.com</span>
        </li>
      </ul>
    </footer>
  </section>
</main>
</body>
</html>
```